Healthcare and Professional IT Services Company need a redesigned business card

We are a IT Services company that targets small medical practices and professional business such as Attorneys, Accounts, Architects etc. We want to communicate a professional yet friendly image using recent logo redesign here on Drafthive. Like to see the colors blue and orange in the design. Must use the Tall Cedar Technology as displayed in the new logo - then also want to incorporate the fish logo as well.

Target Market(s)

Small medical and professional services

Industry/Entity Type

It Company

Contact Information for Business Card

The usual stuff, place for name address phone website. Also maybe our tagline which is "rooted in technology"

Requirements
Must have
• My new logo and the fish somewhere on the card

```html
<!DOCTYPE html>
<html lang="en">
<head>
<meta charset="utf-8">
<title>Tall Cedar Technology – Business Card</title>
<link rel="stylesheet" href="https://fonts.googleapis.com/css2?family=Open+Sans:wght@400;600;700&display=swap">
<style>
  :root {
    --stage: #232426;
    --brand-blue: #0f93d6;
    --brand-blue-deep: #0a7fc0;
    --brand-orange: #f29a1f;
    --paper: #ffffff;
    --paper-shade: #eef1f3;
    --ink-white: #ffffff;
  }
  * { margin: 0; padding: 0; box-sizing: border-box; }
  html, body { width: 1200px; height: 871px; overflow: hidden; }
  body {
    background: var(--stage);
    font-family: "Open Sans", Arial, sans-serif;
    position: relative;
  }
  .card {
    position: absolute;
    width: 525px;
    height: 300px;
    border-radius: 3px;
    overflow: hidden;
    box-shadow: 0 18px 40px rgba(0,0,0,0.45);
  }
  .card--back {
    left: 50px;
    top: 285px;
    background: linear-gradient(135deg, var(--brand-blue-deep), var(--brand-blue) 60%, #2aa4e0);
    display: flex;
    flex-direction: column;
    align-items: center;
    justify-content: center;
    color: var(--ink-white);
  }
  .back-brand {
    display: flex;
    align-items: center;
    gap: 12px;
    font-size: 30px;
    font-weight: 600;
    letter-spacing: 0.5px;
  }
  .back-brand .mark-dot {
    width: 22px; height: 22px;
    border-radius: 50%;
    background: var(--ink-white);
  }
  .tagline {
    margin-top: 28px;
    font-size: 15px;
    font-weight: 600;
    letter-spacing: 0.3px;
  }
  .card--front {
    left: 625px;
    top: 285px;
    background: linear-gradient(180deg, var(--paper), var(--paper-shade));
  }
  .front-identity {
    position: absolute;
    left: 0; right: 0; top: 0;
    height: 186px;
    display: flex;
    flex-direction: column;
    align-items: center;
    justify-content: flex-end;
    padding-bottom: 10px;
  }
  .front-brand {
    display: flex;
    align-items: center;
    gap: 10px;
    color: var(--brand-blue);
    font-size: 26px;
    font-weight: 600;
    margin-bottom: 18px;
  }
  .front-brand .mark-dot {
    width: 18px; height: 18px;
    border-radius: 50%;
    background: var(--brand-blue);
  }
  .person-name {
    color: var(--brand-blue);
    font-size: 17px;
    font-weight: 700;
    line-height: 1.2;
  }
  .person-title {
    color: var(--brand-orange);
    font-size: 13px;
    font-weight: 600;
  }
  .contact-band {
    position: absolute;
    left: 0; right: 0; bottom: 0;
    height: 114px;
    background: linear-gradient(180deg, var(--brand-blue), var(--brand-blue-deep));
    border-top: 3px solid var(--brand-orange);
    color: var(--ink-white);
    font-size: 12.5px;
    display: flex;
    flex-direction: column;
    justify-content: center;
    align-items: center;
    gap: 8px;
  }
  .contact-line span + span { margin-left: 14px; }
</style>
</head>
<body>
  <section class="card card--back" aria-label="Business card back">
    <div class="back-brand"><span class="mark-dot"></span>Tall Cedar Technology</div>
    <p class="tagline">rooted in technology</p>
  </section>

  <section class="card card--front" aria-label="Business card front">
    <div class="front-identity">
      <div class="front-brand"><span class="mark-dot"></span>Tall Cedar Technology</div>
      <p class="person-name">Owen Marsh</p>
      <p class="person-title">President</p>
    </div>
    <div class="contact-band">
      <p class="contact-line">2417 Harbor Crest Lane, Millbrook, NY 12545</p>
      <p class="contact-line">
        <span>P : 555 0142 7781</span>
        <span>E : owen@tallcedar.example</span>
        <span>W : www.tallcedar.example</span>
      </p>
    </div>
  </section>
</body>
</html>
```